UI design for kiosk touch screen

We need a UI design for a touch screen device to be used by costumers in a store and show information about specific products. We're looking for a general concept to serve as a starting point and we're not expecting a fully coded design.
We envision a UI where it first shows a range of products; once touched, it should show information about the product which includes text, touchable photos, videos and document files. We're interested in the starting page and the product details page.
We are the suppliers of the device and not the owners of stores that will use them. The purpose of this design is for in-person demonstrations to potential clients or in ads so the design should be agnostic about the end product(s). You may freely pick random placeholder or fictional products and assets to showcase the design concept as long as they can be changed without compromising the design. You can use our logo (annexed) in the design as a placeholder but it's not necessary.
We're using web technologies to develop the UI so the same principles should apply, except some exceptions below:
- There's no need for a responsive design since the resolution is set at 1920x1080 on a 22'' monitor in landscape orientation.
- All interactions will be done using the touchscreen, so any interactive component needs to be large enough for navigation to be comfortable.
- The design should be visually engaging and eye-catching, more so than a regular website.
Physical shop owners.
Store
2 page

```html
<!DOCTYPE html>
<html lang="en">
<head>
<meta charset="utf-8">
<title>Norvex Kiosk – Product Details</title>
<link href="https://fonts.googleapis.com/css2?family=Open+Sans:wght@400;600;700&display=swap" rel="stylesheet">
<style>
  :root{
    --header-top:#a6eefb;
    --header-bottom:#d8f6fd;
    --page-bg-1:#e9eef5;
    --page-bg-2:#dce5f1;
    --blue:#1a8cf0;
    --blue-dark:#0f74d4;
    --orange:#f7931e;
    --orange-price:#f7891f;
    --text-dark:#2b2b2b;
    --text-mid:#5a5a5a;
    --text-soft:#8c8c8c;
    --star:#f6b500;
    --star-off:#c9c9c9;
    --tab-active:#6e6e6e;
    --tab-bg:#e6f2fb;
    --panel-top:#ffffff;
    --panel-bottom:#cfe9f8;
    --card-bottom:#c9dcf7;
    --photo-dark:#2d3136;
    --photo-mid:#55595e;
  }
  *{box-sizing:border-box;margin:0;padding:0}
  html,body{width:1200px;height:672px;overflow:hidden}
  body{
    font-family:'Open Sans',sans-serif;
    background:linear-gradient(160deg,var(--page-bg-1),var(--page-bg-2));
    position:relative;color:var(--text-dark);
  }
  .header{
    position:absolute;left:0;top:0;width:1200px;height:98px;
    background:linear-gradient(180deg,var(--header-top),var(--header-bottom));
    box-shadow:0 2px 6px rgba(0,0,0,.12);
  }
  .brand{position:absolute;left:105px;top:32px;display:flex;align-items:center;gap:10px}
  .brand-mark{width:30px;height:30px;background:var(--blue);border-radius:4px}
  .brand-name{font-size:30px;font-weight:700;color:var(--blue);letter-spacing:1px}
  .btn{
    position:absolute;display:flex;align-items:center;justify-content:center;gap:6px;
    background:var(--blue);color:#fff;font-weight:700;border-radius:2px;
  }
  .btn-search{left:905px;top:30px;width:87px;height:37px;font-size:16px}
  .btn-list{left:1005px;top:30px;width:87px;height:34px;font-size:15px;border-radius:2px 2px 0 0}
  .list-rule{position:absolute;left:1005px;top:63px;width:166px;height:2px;background:var(--blue)}
  .list-panel{
    position:absolute;left:1005px;top:65px;width:166px;height:188px;background:#fff;
    box-shadow:0 2px 6px rgba(0,0,0,.15);padding:8px 10px;z-index:2
  }
  .list-panel .count{font-size:12px;line-height:12px;color:var(--text-mid);padding-bottom:5px;border-bottom:1px solid #ddd}
  .list-item{display:flex;gap:12px;padding:10px 0 8px;border-bottom:1px solid #ddd}
  .list-thumb{width:50px;height:42px;background:linear-gradient(90deg,var(--photo-dark),var(--photo-mid))}
  .list-info{font-size:9.5px;line-height:11px;color:var(--text-mid)}
  .list-info b{display:block;margin-top:3px;color:var(--text-dark);font-weight:600}
  .list-total{font-size:11px;margin-top:6px;color:var(--text-dark)}
  .list-total b{font-weight:700}

  .hero{
    position:absolute;left:104px;top:120px;width:450px;height:219px;
    background:linear-gradient(90deg,#7d8084,#5b5f64 45%,#3b3f45 60%,#8a8c8f);
  }
  .hero svg{position:absolute;left:193px;top:77px}
  .thumb{position:absolute;top:357px;width:105px;height:87px;border:1px solid #cfd3d8;padding:4px;background:#f3f3f3}
  .thumb div{width:100%;height:100%;background:linear-gradient(90deg,#c9c6c0,var(--photo-dark) 30%,var(--photo-dark) 70%,#c9c6c0)}

  .title{position:absolute;left:581px;top:112px;font-size:27px;font-weight:400;color:var(--text-mid)}
  .stars{display:flex;gap:2px;color:var(--star)}
  .stars .off{color:var(--star-off)}
  .detail-stars{position:absolute;left:582px;top:158px;font-size:15px}
  .prices{position:absolute;left:583px;top:183px;display:flex;align-items:baseline;gap:12px}
  .old{color:var(--text-soft);text-decoration:line-through;font-size:16px}
  .new{color:var(--orange-price);font-size:22px;font-weight:600}
  .btn-size{left:583px;top:222px;width:52px;height:31px;font-size:12px}
  .btn-add{left:648px;top:222px;width:107px;height:31px;font-size:12px}

  .tabs{position:absolute;left:583px;top:272px;display:flex;height:37px}
  .tab{display:flex;align-items:center;justify-content:center;font-size:15px;color:var(--text-mid);
    background:var(--tab-bg);border-right:1px solid #c7d8e6}
  .tab.active{background:var(--tab-active);color:#fff}
  .tab-body{
    position:absolute;left:583px;top:309px;width:509px;height:135px;padding:14px 15px;
    background:linear-gradient(180deg,var(--panel-top),var(--panel-bottom));
    font-size:12px;line-height:19.3px;color:var(--text-mid);box-shadow:0 1px 4px rgba(0,0,0,.1)
  }

  .section-title{position:absolute;left:103px;top:455px;font-size:26px;font-weight:600;color:var(--text-dark)}
  .arrow{position:absolute;top:460px;width:20px;height:20px;border-radius:50%;background:var(--orange)}
  .arrow svg{display:block}

  .card{position:absolute;top:499px;width:146px;height:162px;
    background:linear-gradient(180deg,#fff 55%,var(--card-bottom));box-shadow:0 1px 4px rgba(0,0,0,.15)}
  .card-img{height:85px;position:relative}
  .badge{position:absolute;right:5px;bottom:-10px;width:20px;height:20px;border-radius:50%;background:var(--orange);
    color:#fff;font-size:6.5px;font-weight:700;display:flex;align-items:center;justify-content:center}
  .card-name{padding:8px 8px 0;font-size:12.5px;line-height:14px;font-weight:600;color:var(--text-mid);height:40px}
  .card-stars{padding:0 8px;font-size:10px}
  .card-prices{padding:4px 8px 0;display:flex;align-items:baseline;gap:6px}
  .card-prices .old{font-size:11px}
  .card-prices .new{font-size:15px}
</style>
</head>
<body>
  <header class="header">
    <div class="brand"><span class="brand-mark"></span><span class="brand-name">Norvex</span></div>
  </header>

  <div class="btn btn-search">
    <svg width="13" height="13" viewBox="0 0 14 14"><circle cx="6" cy="6" r="4.5" fill="none" stroke="#fff" stroke-width="1.6"/><line x1="9.3" y1="9.3" x2="13" y2="13" stroke="#fff" stroke-width="1.8"/></svg>
    Search
  </div>
  <div class="btn btn-list">
    <svg width="15" height="12" viewBox="0 0 15 12" fill="#fff"><rect x="0" y="0" width="2" height="2"/><rect x="4" y="0" width="11" height="2"/><rect x="0" y="5" width="2" height="2"/><rect x="4" y="5" width="11" height="2"/><rect x="0" y="10" width="2" height="2"/><rect x="4" y="10" width="11" height="2"/></svg>
    My List
  </div>
  <div class="list-rule"></div>
  <aside class="list-panel">
    <p class="count">You have 2 items in your List</p>
    <div class="list-item">
      <div class="list-thumb" role="img" aria-label="Dark raw denim jeans photo"></div>
      <div class="list-info">Mens Skinny Slim Raw Jeans<b>Price: $476</b></div>
    </div>
    <div class="list-item">
      <div class="list-thumb" role="img" aria-label="Dark raw denim jeans photo"></div>
      <div class="list-info">Mens Skinny Slim Raw Jeans<b>Price: $476</b></div>
    </div>
    <p class="list-total"><b>Total</b> : $952</p>
  </aside>

  <div class="hero" role="img" aria-label="Product video: model wearing black tee and raw denim jeans">
    <svg width="64" height="64" viewBox="0 0 64 64"><circle cx="32" cy="32" r="29" fill="none" stroke="#fff" stroke-width="4"/><path d="M26 19 L46 32 L26 45 Z" fill="#fff"/></svg>
  </div>
  <div class="thumb" style="left:104px"><div role="img" aria-label="Jeans front close-up photo"></div></div>
  <div class="thumb" style="left:219px"><div role="img" aria-label="Full outfit photo"></div></div>
  <div class="thumb" style="left:334px"><div role="img" aria-label="Jeans legs photo"></div></div>
  <div class="thumb" style="left:449px"><div role="img" aria-label="Jeans back pocket photo"></div></div>

  <h1 class="title">Mens Skinny Slim Raw Jeans</h1>
  <div class="stars detail-stars">★★★★<span class="off">★</span></div>
  <div class="prices"><span class="old">$1,999</span><span class="new">$476</span></div>
  <div class="btn btn-size">Size <svg width="9" height="7" viewBox="0 0 9 7"><path d="M0 0H9L4.5 7Z" fill="#fff"/></svg></div>
  <div class="btn btn-add"><svg width="10" height="10" viewBox="0 0 10 10"><path d="M4 0h2v10H4zM0 4h10v2H0z" fill="#fff"/></svg>Add to Mylist</div>

  <nav class="tabs">
    <div class="tab active" style="width:122px">Overview</div>
    <div class="tab" style="width:127px">Features</div>
    <div class="tab" style="width:153px">Specification</div>
    <div class="tab" style="width:107px;border-right:0">Review</div>
  </nav>
  <div class="tab-body">The best things in life are custom. You can rely on our new classic Skinny Slim 14 oz. raw selvedge indigo denim to evolve over time, gradually taking on characteristics unique only to its wearer. Treated to prevent future shrinkage, our raw fabric is infused with 2% spandex stretch for comfort rarely seen in premium selvedge denim. Our Skinny Slim fit jean hugs the thigh and tapers from knee to ankle for a tailored look.</div>

  <h2 class="section-title">Recomended</h2>
  <div class="arrow" style="left:1046px"><svg width="20" height="20" viewBox="0 0 20 20"><path d="M11.5 6L7.5 10L11.5 14" fill="none" stroke="#fff" stroke-width="1.6"/></svg></div>
  <div class="arrow" style="left:1072px"><svg width="20" height="20" viewBox="0 0 20 20"><path d="M8.5 6L12.5 10L8.5 14" fill="none" stroke="#fff" stroke-width="1.6"/></svg></div>

  <article class="card" style="left:104px">
    <div class="card-img" role="img" aria-label="Model in white crew neck tee" style="background:linear-gradient(180deg,#dcdcdc,#f4f4f4)"><span class="badge">-60%</span></div>
    <h3 class="card-name">Mens Crew Neck Tee White</h3>
    <div class="stars card-stars">★★★★★</div>
    <div class="card-prices"><span class="old">$1,999</span><span class="new">$476</span></div>
  </article>
  <article class="card" style="left:273px">
    <div class="card-img" role="img" aria-label="Model in black crew neck tee" style="background:linear-gradient(180deg,#cfcfcf,#2a2a2a)"><span class="badge">-60%</span></div>
    <h3 class="card-name">Mens Crew Neck Tee Black</h3>
    <div class="stars card-stars">★★★★★</div>
    <div class="card-prices"><span class="old">$1,999</span><span class="new">$476</span></div>
  </article>
  <article class="card" style="left:441px">
    <div class="card-img" role="img" aria-label="Beige chino shorts" style="background:linear-gradient(180deg,#ffffff,#ddd6cf)"><span class="badge">-60%</span></div>
    <h3 class="card-name">Mens Skinny Slim Short</h3>
    <div class="stars card-stars">★★★★★</div>
    <div class="card-prices"><span class="old">$1,999</span><span class="new">$476</span></div>
  </article>
  <article class="card" style="left:610px">
    <div class="card-img" role="img" aria-label="Model in white selvedge chinos" style="background:linear-gradient(180deg,#4a4d52,#e8e8e8)"><span class="badge">-60%</span></div>
    <h3 class="card-name">Mens Skinny Slim Selvedge Chino</h3>
    <div class="stars card-stars">★★★★★</div>
    <div class="card-prices"><span class="old">$1,999</span><span class="new">$476</span></div>
  </article>
  <article class="card" style="left:778px">
    <div class="card-img" role="img" aria-label="Model in black selvedge chino pants" style="background:linear-gradient(180deg,#2b2b2b,#3d3d3d 60%,#e6e6e6)"><span class="badge">-60%</span></div>
    <h3 class="card-name">Mens Skinny Slim Selvedge Chino Pant</h3>
    <div class="stars card-stars">★★★★★</div>
    <div class="card-prices"><span class="old">$1,999</span><span class="new">$476</span></div>
  </article>
  <article class="card" style="left:946px">
    <div class="card-img" role="img" aria-label="Light pink baseball cap" style="background:linear-gradient(180deg,#d9cbc9,#ecebeb)"><span class="badge">-60%</span></div>
    <h3 class="card-name">Mens Skinny Slim Hat</h3>
    <div class="stars card-stars">★★★★★</div>
    <div class="card-prices"><span class="old">$1,999</span><span class="new">$476</span></div>
  </article>
</body>
</html>
```